A pop-banner and Image for a magazine

Pop-up 100cm x 200cm:
Harbourvale Junior Ensembles
Circle of Sound Scheme
Give the Gift of Music

Supporter – €100
Contributes to rehearsal space, music and essential administration.

Champion – €250
Funds coaching, instrument supports and performance opportunities.

Patron – €450
Sponsors a full membership for a young musician where cost is a barrier.

All Circle of Sound Members are acknowledged in concert programmes.
Graphic for Magazine - A4:
HJE - Circle of Sound Scheme
Give the gift of music this year

Circle of Sound – Supporter (€100)
A Supporter helps with the core running costs of HJE such as rehearsal space, music purchase and essential administration. This contribution strengthens the day-to-day foundation that allows over 300 young musicians to learn and perform. Supporters are acknowledged in concert programmes.
Circle of Sound – Champion (€250)
Champions provide deeper backing that directly enhances the musical experience for our ensembles. This level helps fund sectional coaching, instrument supports and performance opportunities. Champions are acknowledged in our programmes and receive an annual note of thanks outlining the impact of their contribution.
Circle of Sound – Patron (€450)
Our Patron tier directly supports social inclusion and participation within HJE. A contribution at this level helps fund a full membership place for a young musician who would otherwise be unable to take part due to financial barriers.
By becoming a Patron, you ensure that every talented player has the chance to rehearse, perform and grow within the orchestra. Patrons are acknowledged in concert programmes and receive priority notice of major events, along with a yearly update on the positive impact of their support.

Industry/Entity Type

Music - please refer to the website for logo and colours

Requirements
Must have
• https://www.hje-example.ie/

```html
<!DOCTYPE html>
<html lang="en">
<head>
<meta charset="utf-8">
<title>Harbourvale Junior Ensembles – Circle of Sound Scheme</title>
<link href="https://fonts.googleapis.com/css2?family=Poppins:wght@400;500;600;700;800&display=swap" rel="stylesheet">
<style>
  :root {
    --stage: #c9ccc9;
    --purple-deep: #4a2170;
    --purple: #6a2f8e;
    --magenta: #a8337f;
    --pink-deep: #d6286a;
    --pink: #ec3a80;
    --pink-text: #f2307a;
    --white: #ffffff;
    --ink: #3a2a78;
    --rule: rgba(255,255,255,0.75);
  }
  * { box-sizing: border-box; margin: 0; padding: 0; }
  html, body {
    width: 1200px; height: 800px; overflow: hidden;
    background: var(--stage);
    font-family: "Poppins", sans-serif;
  }
  .flyer {
    position: absolute; left: 324px; top: 10px;
    width: 551px; height: 780px; overflow: hidden;
    background: linear-gradient(180deg, var(--purple-deep) 0%, var(--purple) 30%, var(--magenta) 62%, var(--pink-deep) 90%);
    color: var(--white);
    box-shadow: 0 10px 24px rgba(0,0,0,0.25);
  }
  .backdrop-photo {
    position: absolute; left: 0; top: 0; width: 100%; height: 330px;
    background: linear-gradient(180deg, rgba(40,18,70,0.55) 0%, rgba(110,50,150,0.25) 70%, rgba(110,50,150,0) 100%);
  }
  .brand { position: absolute; left: 40px; top: 40px; display: flex; align-items: flex-start; gap: 10px; }
  .brand-mark { width: 52px; height: 52px; background: var(--white); flex: none; }
  .brand-name { font-weight: 600; font-size: 18px; line-height: 21px; }
  .brand-sub { font-weight: 600; font-size: 8px; line-height: 14px; margin-top: 2px; }
  .site-url { position: absolute; right: 40px; top: 26px; font-size: 15px; font-weight: 500; }
  .programme { position: absolute; left: 40px; top: 138px; }
  .programme-lead { font-size: 25px; font-weight: 400; line-height: 31px; }
  .programme-name { font-size: 25px; font-weight: 700; line-height: 31px; color: var(--pink-text); }
  .headline-band {
    position: absolute; left: 41px; top: 216px; width: 394px; height: 111px;
    background: var(--pink); padding: 9px 0 0 15px;
  }
  .headline {
    font-size: 49px; font-weight: 800; line-height: 46px; letter-spacing: -0.5px; text-transform: uppercase;
  }
  .guitar-photo {
    position: absolute; left: 420px; top: 52px; width: 98px; height: 284px;
    border-radius: 40px 40px 46px 46px;
    background: linear-gradient(180deg, rgba(120,80,40,0.5) 0%, #c9a66b 55%, #e2c690 75%, #4a2a18 100%);
  }
  .tier { position: absolute; left: 40px; width: 472px; height: 120px; }
  .tier-icon { position: absolute; left: 0; top: -4px; width: 34px; height: 52px; }
  .tier-label { position: absolute; left: 43px; top: 0; font-size: 12.5px; font-weight: 600; line-height: 15px; }
  .tier-name { position: absolute; left: 43px; top: 14px; font-size: 26px; font-weight: 700; line-height: 34px; }
  .tier-price {
    position: absolute; left: 43px; top: 53px; width: 153px; height: 31px;
    border: 2px solid var(--white); border-radius: 16px; background: var(--pink-deep);
    font-size: 25px; font-weight: 700; line-height: 27px; text-align: center;
  }
  .tier-text { position: absolute; left: 222px; top: -7px; width: 252px; font-size: 10.4px; line-height: 12.2px; }
  .tier-rule { position: absolute; left: 40px; width: 472px; height: 1px; background: var(--rule); }
  .footer {
    position: absolute; left: 0; bottom: 0; width: 100%; height: 74px;
    background: var(--white); color: var(--ink);
    font-size: 9.3px; line-height: 11px; text-align: center; padding: 16px 46px 0;
  }
</style>
</head>
<body>
  <main class="flyer">
    <div class="backdrop-photo" role="img" aria-label="Photograph of young orchestra musicians playing string instruments, tinted purple"></div>

    <header class="brand">
      <div class="brand-mark"></div>
      <div>
        <div class="brand-name">Harbourvale Junior<br>Ensembles</div>
        <div class="brand-sub">Ceolfhoirne Óga Chuanbhaile</div>
      </div>
    </header>
    <div class="site-url">www.hje-example.ie</div>

    <div class="programme">
      <div class="programme-lead">Circle of Sound</div>
      <div class="programme-name">Scheme</div>
    </div>

    <div class="headline-band">
      <h1 class="headline">Give the gift<br>of music</h1>
    </div>
    <div class="guitar-photo" role="img" aria-label="Photograph of an acoustic guitar standing upright"></div>

    <section class="tier" style="top:361px">
      <svg class="tier-icon" viewBox="0 0 34 52"><ellipse cx="11" cy="43" rx="10" ry="8" fill="#fff" transform="rotate(-20 11 43)"/><rect x="18" y="2" width="3" height="41" fill="#fff"/><path d="M21 2 C24 10 33 14 31 26 C30 20 26 17 21 15 Z" fill="#fff"/></svg>
      <div class="tier-label">Circle of Sound –</div>
      <div class="tier-name">Supporter</div>
      <div class="tier-price">€100</div>
      <p class="tier-text">A Supporter helps with the core running costs of HJE such as rehearsal space, music purchase and essential administration. This contribution strengthens the day-to-day foundation that allows over 300 young musicians to learn and perform. Supporters are acknowledged in concert programmes.</p>
    </section>
    <div class="tier-rule" style="top:458px"></div>

    <section class="tier" style="top:486px">
      <svg class="tier-icon" viewBox="0 0 34 52"><ellipse cx="11" cy="43" rx="10" ry="8" fill="#fff" transform="rotate(-20 11 43)"/><rect x="18" y="2" width="3" height="41" fill="#fff"/><path d="M21 2 C24 10 33 14 31 26 C30 20 26 17 21 15 Z" fill="#fff"/></svg>
      <div class="tier-label">Circle of Sound –</div>
      <div class="tier-name">Champion</div>
      <div class="tier-price">€250</div>
      <p class="tier-text">Champions provide deeper backing that directly enhances the musical experience for our ensembles. This level helps fund sectional coaching, instrument supports and performance opportunities. Champions are acknowledged in our programmes and receive an annual note of thanks outlining the impact of their contribution.</p>
    </section>
    <div class="tier-rule" style="top:591px"></div>

    <section class="tier" style="top:613px">
      <svg class="tier-icon" viewBox="0 0 34 52"><ellipse cx="11" cy="43" rx="10" ry="8" fill="#fff" transform="rotate(-20 11 43)"/><rect x="18" y="2" width="3" height="41" fill="#fff"/><path d="M21 2 C24 10 33 14 31 26 C30 20 26 17 21 15 Z" fill="#fff"/></svg>
      <div class="tier-label">Circle of Sound –</div>
      <div class="tier-name">Patron</div>
      <div class="tier-price">€450</div>
      <p class="tier-text">Our Patron tier directly supports social inclusion and participation within HJE. A contribution at this level helps fund a full membership place for a young musician who would otherwise be unable to take part due to financial barriers.</p>
    </section>

    <footer class="footer">
      By becoming a Patron, you ensure that every talented player has the chance to rehearse, perform and grow within the orchestra. Patrons are acknowledged in concert programmes and receive priority notice of major events, along with a yearly update on the positive impact of their support.
    </footer>
  </main>
</body>
</html>
```